E brochure for company overview

We need a brochure for a company overview that will be sent to potential new clients. We are uploading a file with all the content that needs to be included inside of the brochure. We need this content to be displayed in a professional, neat, and creative way. The file has a Spanish and English version so we need two versions of the brochure in each language. *This brochure will be viewed digitally and it will not be printed, thus it does not need a cover page*. We included our company logo (Calvenor) Please utilize this in your design.

```html
<!DOCTYPE html>
<html lang="en">
<head>
<meta charset="UTF-8">
<title>Calvenor – Company Overview</title>
<link href="https://fonts.googleapis.com/css2?family=Barlow:wght@300;400;500;600;700&family=Arimo:wght@400;700&display=swap" rel="stylesheet">
<style>
  :root{
    --canvas:#e9e9e9;
    --ink-dark:#0b0b0b;
    --ink-mid:#1e1e1e;
    --red:#e0302c;
    --white:#ffffff;
    --text-light:#f2f2f2;
    --grey-1:#6f6f6f;
    --grey-2:#8c8c8c;
    --grey-3:#bdbdbd;
    --label-grey:#555555;
    --logo-dark:#2b2b2b;
    --partner-green:#234540;
    --partner-blue:#1d8fd6;
  }
  *{margin:0;padding:0;box-sizing:border-box}
  html,body{width:1000px;height:1200px;overflow:hidden;background:var(--canvas)}
  .brochure{position:absolute;left:118px;top:106px;width:764px;height:989px;overflow:hidden;background:var(--white);font-family:"Arimo",Arial,sans-serif}
  .brochure__dark{position:absolute;left:0;top:0;width:764px;height:872px;
    background:radial-gradient(ellipse at 75% 45%,#3a3a3a 0%,#1c1c1c 45%,var(--ink-dark) 80%)}
  .brochure__texture{position:absolute;left:400px;top:0;width:364px;height:872px;
    background:radial-gradient(circle at 80% 50%,rgba(90,90,90,.25),rgba(0,0,0,0) 60%)}
  .brochure__shapes{position:absolute;left:0;top:0}
  .section-title{position:absolute;font-family:"Barlow",sans-serif;font-weight:500;font-size:21px;letter-spacing:1.2px;color:var(--red)}
  .rule{position:absolute;height:1px;background:var(--white)}
  .lead{position:absolute;font-weight:700;font-size:16px;color:var(--white)}
  .copy{position:absolute;font-size:13px;line-height:17.5px;color:var(--text-light)}
  .services{position:absolute;left:317px;top:601px;width:420px;text-align:center;font-size:13.5px;line-height:22.5px;color:var(--text-light)}
  .services .sep{color:var(--red);margin:0 7px}
  .value{position:absolute;font-family:"Barlow",sans-serif;font-weight:400;line-height:1;white-space:nowrap}
  .value--teamwork{left:437px;top:718px;font-size:45px;color:var(--grey-1)}
  .value--attitude{left:242px;top:766px;font-size:36px;color:var(--white)}
  .value--integrity{left:577px;top:768px;font-size:30px;color:var(--grey-2)}
  .value--commitment{left:303px;top:816px;font-size:25px;color:var(--grey-3)}
  .value--creativity{left:477px;top:807px;font-size:37px;color:var(--grey-1)}
  .brand{position:absolute;left:35px;top:399px;width:240px;text-align:center}
  .brand__mark{width:70px;height:70px;border-radius:50%;background:var(--red);margin:0 auto 14px}
  .brand__name{font-family:"Barlow",sans-serif;font-weight:600;font-size:41px;line-height:1;letter-spacing:.5px;color:var(--logo-dark)}
  .brand__tagline{margin-top:6px;font-family:"Barlow",sans-serif;font-weight:500;font-size:13px;letter-spacing:.6px;color:var(--logo-dark)}
  .partners__label{position:absolute;left:172px;top:892px;width:90px;text-align:right;font-family:"Barlow",sans-serif;font-size:14px;line-height:16px;letter-spacing:1.3px;color:var(--label-grey)}
  .partners__rule{position:absolute;left:172px;top:937px;width:90px;height:1px;background:var(--label-grey)}
  .partner{position:absolute;font-family:"Barlow",sans-serif;line-height:1;white-space:nowrap}
  .partner--bridgeport{left:298px;top:898px;font-size:24px;font-weight:700;letter-spacing:.5px;color:var(--ink-mid)}
  .partner--flowcrest{left:330px;top:933px;font-size:24px;font-weight:600;color:var(--partner-green)}
  .partner--tessora{left:517px;top:906px;font-size:34px;font-weight:600;color:var(--ink-mid)}
  .partner--halvern{left:640px;top:911px;font-size:26px;font-weight:600;color:var(--partner-blue)}
</style>
</head>
<body>
<main class="brochure">
  <div class="brochure__dark"></div>
  <div class="brochure__texture" role="img" aria-label="Faint dotted wave texture on dark background"></div>

  <svg class="brochure__shapes" width="764" height="989" viewBox="0 0 764 989" aria-hidden="true">
    <defs>
      <linearGradient id="band-gradient" x1="0" y1="0" x2="1" y2="0">
        <stop offset="0" stop-color="#f26a22"/>
        <stop offset="0.35" stop-color="#e0302c"/>
        <stop offset="1" stop-color="#d0231f"/>
      </linearGradient>
    </defs>
    <rect x="0" y="872" width="764" height="117" fill="#ffffff"/>
    <polygon points="0,0 90,0 382,490 90,989 0,989" fill="url(#band-gradient)"/>
    <polygon points="0,112 314,490 0,874" fill="#ffffff"/>
  </svg>

  <div class="brand">
    <div class="brand__mark"></div>
    <div class="brand__name">CALVENOR</div>
    <div class="brand__tagline">IT CONSULTING AND SERVICES</div>
  </div>

  <h2 class="section-title" style="left:180px;top:62px">HISTORY</h2>
  <div class="rule" style="left:243px;top:93px;width:90px"></div>
  <p class="lead" style="left:243px;top:104px">Calvenor initiates on 2006</p>
  <p class="copy" style="left:243px;top:126px;width:470px">Calvenor has 15 years in the technology industry , specialising in security management, infrastructure and service management.</p>

  <h2 class="section-title" style="left:244px;top:211px">MISSION</h2>
  <div class="rule" style="left:303px;top:243px;width:90px"></div>
  <p class="copy" style="left:303px;top:251px;width:400px">Providing our customers with the best human and technological resources with the clear objective of providing effective solutions using best industry practices .</p>

  <h2 class="section-title" style="left:350px;top:354px">VISSION</h2>
  <div class="rule" style="left:412px;top:386px;width:90px"></div>
  <p class="copy" style="left:412px;top:397px;width:290px">To be recognized by our customers as an important company in the Dominican Republic in the area of security and infrastructure and achieve presence throughout the Caribbean and Central America.</p>

  <h2 class="section-title" style="left:350px;top:546px">OUR SERVICES</h2>
  <div class="rule" style="left:412px;top:579px;width:90px"></div>
  <p class="services">
    Service Management<span class="sep">|</span>Security of Information<br>
    Custom Development<span class="sep">|</span>Devops<span class="sep">|</span>Staffing<br>
    Device and Network Monitoring<span class="sep">|</span>API Management
  </p>

  <h2 class="section-title" style="left:261px;top:720px;font-size:22px">OUR VALUES</h2>
  <div class="rule" style="left:324px;top:752px;width:90px"></div>
  <span class="value value--teamwork">TEAM WORK</span>
  <span class="value value--attitude">POSITIVE ATTITUDE</span>
  <span class="value value--integrity">INTEGRITY</span>
  <span class="value value--commitment">COMMITMENT</span>
  <span class="value value--creativity">CREATIVITY</span>

  <div class="partners__label">OUR<br>PARTNERS</div>
  <div class="partners__rule"></div>
  <div class="partner partner--bridgeport">BRIDGEPORT</div>
  <div class="partner partner--flowcrest">flowcrest</div>
  <div class="partner partner--tessora">tessora</div>
  <div class="partner partner--halvern">halvern</div>
</main>
</body>
</html>
```